Education business partners flyer

Our service is New Zealand education and migration. We are trying to recruit business partners from around the world who can refer clients to us. We need a 2-3 page PDF flyer that we want to share with our prospective partners. Our content is ready (file attached). It needs to be designed well with relevant NZ images, international students/migrants and our logo of course.

Target Market(s)

All around the world

Industry/Entity Type

Education

Font styles to use
Sans Serif

Colors

Designer to choose colors to be used in the design.

Requirements
Must have
• It needs to be designed well with relevant NZ images, international students/migrants and our logo of course.
Nice to have
• Copyright free images.
Should not have
• Images with any copyright issues.

```html
<!DOCTYPE html>
<html lang="en">
<head>
<meta charset="utf-8">
<title>KVT Services – Partnership Proposal</title>
<link href="https://fonts.googleapis.com/css2?family=Jost:wght@400;500;600;700&display=swap" rel="stylesheet">
<style>
:root{
  --backdrop:#b5a8c9;
  --paper:#ffffff;
  --purple:#6a3f9b;
  --purple-deep:#5a2f8c;
  --lavender:#e7dcf6;
  --lavender-soft:#f4eefb;
  --ink:#3a3a3a;
  --ink-soft:#555;
  --rule:#cfc3e0;
}
*{margin:0;padding:0;box-sizing:border-box}
html,body{width:918px;height:1200px;overflow:hidden}
body{background:var(--backdrop);font-family:"Jost",Arial,sans-serif;color:var(--ink);position:relative}
.page{position:absolute;width:416px;height:538px;background:var(--paper);overflow:hidden}
.page--one{left:34px;top:42px;padding:0 12px 0 18px}
.page--two{left:475px;top:312px;padding:0 22px 0 17px}
.page--three{left:34px;top:618px;padding:0 18px 0 18px}
.top-rule{height:3px;background:var(--purple);margin-left:-1px}
.page--two .top-rule{margin:18px -22px 0 0}
.page--three .top-rule{margin:13px -18px 0 0}

.hero{position:relative;margin-top:14px;width:381px;height:134px;
  background:linear-gradient(100deg,#fbf3dc 0%,#f1d9a0 35%,#d9b36c 60%,#b9885a 100%)}
.brand{position:absolute;left:22px;top:16px;display:flex;align-items:center;gap:5px;
  font-weight:700;font-size:24px;color:var(--ink);letter-spacing:1px}
.brand-dot{width:12px;height:12px;border-radius:50%;background:var(--purple)}
.address{position:absolute;left:14px;top:70px;font-weight:600;font-size:9.4px;line-height:11.5px;color:var(--purple-deep)}
.doc-title{text-align:center;font-weight:600;font-size:6.2px;line-height:9.5px;margin:10px 0 8px;color:#222}

.bar{height:12px;margin:0 0 3px;padding:2px 6px 0;font-size:6px;font-weight:500;color:var(--purple-deep);
  background:linear-gradient(180deg,var(--lavender-soft),var(--lavender));border-bottom:1px solid var(--rule)}
.body{font-size:5.6px;line-height:9.6px;color:var(--ink-soft)}
.section{margin-bottom:11px}
.point{margin-bottom:10px}
.point-title{display:flex;align-items:center;gap:4px;font-size:5.6px;font-weight:600;color:#222;margin-bottom:3px;letter-spacing:.2px}
.tick{width:7px;height:7px;flex:none}
.point .body{padding-left:0}
.page--two .point .body,.page--three .point .body{padding-left:10px}

.diagram{display:block;margin-left:-17px;width:415px;height:210px}
.diagram text{font-family:"Jost",Arial,sans-serif;font-size:5.6px;font-weight:500;fill:#222;letter-spacing:.3px}

.contact-bar{margin-top:10px}
.contact-photo{position:absolute;left:18px;top:287px;width:380px;height:130px;
  background:linear-gradient(90deg,#d9a88a 0%,#e8cfc0 35%,#dfe4ee 65%,#cfd8e8 100%)}
.contact-brand{position:absolute;right:28px;top:14px;width:56px;height:32px;background:#fff;
  display:flex;align-items:center;justify-content:center;gap:3px;font-weight:700;font-size:13px;color:var(--ink)}
.contact-brand .brand-dot{width:6px;height:6px}
.contact-card{position:absolute;left:18px;top:397px;width:144px;height:86px;background:var(--purple);
  padding:14px 0 0 21px;color:#fff;font-size:5.6px}
.contact-row{display:flex;align-items:flex-start;gap:5px;margin-bottom:7px}
.icon{width:10px;height:10px;border-radius:50%;background:rgba(255,255,255,.28);flex:none;display:flex;align-items:center;justify-content:center}
.icon svg{width:6px;height:6px}
.role{display:block;font-style:italic;font-size:5px;opacity:.75;margin-top:2px}
.footer{position:absolute;left:18px;right:18px;top:501px;padding-bottom:4px;border-bottom:1px solid var(--rule);
  font-size:6px;font-weight:600;color:var(--purple-deep)}
</style>
</head>
<body>

<svg width="0" height="0" style="position:absolute">
  <symbol id="tick" viewBox="0 0 10 10"><circle cx="5" cy="5" r="5" fill="#8a8a8a"/><path d="M2.8 5.2 4.4 6.7 7.3 3.6" stroke="#fff" stroke-width="1.3" fill="none"/></symbol>
</svg>

<!-- Page one -->
<section class="page page--one">
  <div class="hero" role="img" aria-label="Photo of a student with a backpack at the doorway of a New Zealand home">
    <div class="brand">KVT<span class="brand-dot"></span></div>
    <p class="address">KVT Services Ltd, 214<br>Harbour Lane,<br>Riverdale, Hamilton,<br>New Zealand - 3216.</p>
  </div>
  <h1 class="doc-title">NEW ZEALAND EDUCATION &amp; MIGRATION BUSINESS OPPORTUNITY<br>PARTNERSHIP PROPOSAL</h1>

  <div class="section">
    <h2 class="bar">Why New Zealand and who is KVT?</h2>
    <p class="body">New Zealand is booming as an education &amp; migration destination. In a world that is spiralling out of control; the serenity, safety and opportunities of New Zealand are attracting people from everywhere like a magnet. Numbers have been growing dramatically year on year. We are a deeply committed New Zealand education &amp; migration company, seeking to attract the best talent from around the world to make New Zealand their new home.</p>
  </div>
  <div class="section">
    <h2 class="bar">Why collaborate with KVT?</h2>
    <p class="body">Collaborations can accelerate mutual growth in a globalised world. Our rationale in this proposal is that we do not have the reach in your market and vice versa you do not have a presence or team in New Zealand to continue to service your students or clients once they arrive here. By coming together we can achieve both these mutual objectives and create a viable and mutual business opportunity.</p>
  </div>
  <div class="section">
    <h2 class="bar">What is the KVT partnership framework?</h2>
    <p class="body">We propose to work with you as our Referral Partner. A partnership that can be mutually beneficial and enhance the value of international education &amp; migration to deserving students and clients from everywhere. Our levels of association can vary depending on your current focus and how you can utilise our position especially in the areas of services that can only be rendered by a Licensed Immigration Adviser.</p>
  </div>
  <div class="section">
    <h2 class="bar">What are the highlights of KVT?</h2>
    <div class="point">
      <h3 class="point-title"><svg class="tick"><use href="#tick"/></svg>We are New Zealand owned and based:</h3>
      <p class="body">Hence we are able to provide services to clients in an end-to-end fashion from suggesting the right courses at the very beginning of their journey to hand-holding them all the way to employment and eventual residency in New Zealand. By working with us you not only create a viable business opportunity but can also be assured that your students/clients are in safe hands after they reach New Zealand. This is where the real challenges start for these young people as they need a huge amount of onshore support and guidance which we can provide.</p>
    </div>
    <div class="point">
      <h3 class="point-title"><svg class="tick"><use href="#tick"/></svg>We have the full range of institutions:</h3>
      <p class="body">We represent the entire gamut of quality New Zealand institutions and in the event your student needs/deserves the appropriate institution to fulfill their future aspirations, we can provide this opportunity for them together. We believe each student deserves to be in the institution that best serves their future interests and we can provide this opportunity for them.</p>
    </div>
  </div>
</section>

<!-- Page two -->
<section class="page page--two">
  <div class="top-rule"></div>
  <svg class="diagram" viewBox="0 0 415 210" aria-label="Service areas diagram">
    <circle cx="207" cy="110" r="70" fill="#e6dcf4"/>
    <circle cx="207" cy="110" r="57" fill="#8a7a6a" role="img" aria-label="Photo of a young man reading a book in a library"/>
    <g fill="#6a3f9b" stroke="#fff" stroke-width="1.5">
      <circle cx="180" cy="48" r="18"/><circle cx="252" cy="59" r="10"/>
      <circle cx="143" cy="107" r="18"/><circle cx="267" cy="121" r="18"/>
      <circle cx="160" cy="151" r="10"/><circle cx="207" cy="174" r="19"/>
    </g>
    <g fill="#fff">
      <circle cx="180" cy="48" r="3.8"/><circle cx="252" cy="59" r="3.2"/>
      <circle cx="143" cy="107" r="3.8"/><circle cx="267" cy="121" r="3.8"/>
      <circle cx="160" cy="151" r="3.2"/><circle cx="207" cy="174" r="3.8"/>
    </g>
    <g stroke="#6a3f9b" stroke-width="1" fill="none">
      <path d="M178.4 48.2 179.6 49.4 181.8 46.8"/><path d="M250.6 59.2 251.6 60.2 253.4 58"/>
      <path d="M141.4 107.2 142.6 108.4 144.8 105.8"/><path d="M265.4 121.2 266.6 122.4 268.8 119.8"/>
      <path d="M158.6 151.2 159.6 152.2 161.4 150"/><path d="M205.4 174.2 206.6 175.4 208.8 172.8"/>
    </g>
    <text x="157" y="46" text-anchor="end">Tour</text>
    <text x="270" y="60">Skill Migration</text>
    <text x="121" y="109" text-anchor="end">Investment Migration</text>
    <text x="289" y="123">Job and Migration</text>
    <text x="144" y="156" text-anchor="end">Business migration</text>
    <text x="207" y="202" text-anchor="middle">Study and settle in</text>
  </svg>

  <div class="point">
    <h3 class="point-title"><svg class="tick"><use href="#tick"/></svg>We have an experienced team and great software:</h3>
    <p class="body">Our competent counseling team backed by a visa team (including ex- New Zealand immigration officers) will ensure that each student is matched to the right course, college, city and to a career of his choice. Your student's parents will be extremely satisfied since their child will be taken care of in a professional manner. We have also built our inhouse software to streamline all processes and partners will have access to their own login for management of their prospects. Not to forget our impressive Board of Advisers who are senior ex- NZ government officials and professionals.</p>
  </div>
  <div class="point">
    <h3 class="point-title"><svg class="tick"><use href="#tick"/></svg>We have a very high visa success rate:</h3>
    <p class="body">Our current visa success rate for the first quarter of 2018 sits well above 90% and we aim to maintain this and keep improving on it successfully. Last year it was 80%. As you are aware a visa process is a detailed legal matter, our processes will ensure that your students have a very high chance of success in their visa applications This means you can focus on your core strength as a marketer and garner prospective students and leave the admission and visa process to an established and successful team.</p>
  </div>
  <div class="point">
    <h3 class="point-title"><svg class="tick"><use href="#tick"/></svg>We have a legal license for all visa types:</h3>
    <p class="body">We are headed by a Licensed immigration Adviser based in New Zealand who was also an IAA Reference Group member for 2017. Our Senior Team members are also getting upgraded towards acquiring their own immigration license. Hence we can assist in all visa types legally. Those without a license simply cannot. For instance international students will need a licensed adviser for their spouse and children visa. We can provide that and this will enable you to gain maximum mileage in your market as someone who can provide a full solution to the entire family.</p>
  </div>
  <div class="point">
    <h3 class="point-title"><svg class="tick"><use href="#tick"/></svg>We are present at every step onshore for clients:</h3>
    <p class="body">We also provide our students and clients with onshore support. Our local team in NZ will guide them with various options for airport pickup, accommodation and part-time job opportunities. Apart from giving ongoing immigration advice during a student's period of stay, we have also been organising a lot of fun activities like networking dinners, picnics and other events. Thus they are assured of a smooth transition towards an eventual NZ residency.</p>
  </div>
</section>

<!-- Page three -->
<section class="page page--three">
  <div class="top-rule"></div>
  <div style="height:12px"></div>
  <div class="point">
    <h3 class="point-title"><svg class="tick"><use href="#tick"/></svg>We are transparent and honest to the core:</h3>
    <p class="body">Our operating principle is to do good to New Zealand, our clients, our partners, our employees and our shareholders in that order. We believe our primary goal is to create a better society in New Zealand and hence we desist from any practice that will hurt this principle. We consistently uphold the integrity of the immigration process of the country and are brutally honest with all stakeholders. Which means you will be partnering with a company that has a zero tolerance for fake documents or clients. As regards money matters too we are fully transparent and none of our partners will ever be given a raw deal.</p>
  </div>
  <div class="point">
    <h3 class="point-title"><svg class="tick"><use href="#tick"/></svg>We are growing and adding new products:</h3>
    <p class="body">At the moment we are only focusing on New Zealand education &amp; migration, but in the coming years we intend to add New Zealand employment, business, investment and tourism opportunities as well. As and when these new products are launched all our existing partner will get the opportunity to refer clients for these too. This means additional revenue to you and an increase in your portfolio of products.</p>
  </div>
  <div class="point">
    <h3 class="point-title"><svg class="tick"><use href="#tick"/></svg>How do we take this forward with KVT?</h3>
    <p class="body">Simple. If you like what you have read so far, respond to our initial mail and our Team Leader - Business Development will revert with a commercial proposal. That can be discussed and once agreeable to both parties we will sign the agreement and proceed to the next stage. This will include training of your staff where needed and initiating other processes.<br><br>We look forward to working with you.<br>Haere mai ki KVT whanau! Welcome to the KVT Family!</p>
  </div>

  <h2 class="bar contact-bar" style="position:absolute;left:18px;right:18px;top:275px;margin:0;color:#222;font-weight:600">For more information, please contact:</h2>
  <div class="contact-photo" role="img" aria-label="Photo of a thoughtful student with glasses and coloured pencils">
    <div class="contact-brand">KVT<span class="brand-dot"></span></div>
  </div>
  <div class="contact-card">
    <div class="contact-row">
      <span class="icon"><svg viewBox="0 0 10 10"><circle cx="5" cy="3.2" r="2.2" fill="#fff"/><path d="M1 10c0-3 2-4.5 4-4.5S9 7 9 10z" fill="#fff"/></svg></span>
      <span>Ms Anika Roswell<span class="role">Team Leader - Business Development</span></span>
    </div>
    <div class="contact-row">
      <span class="icon"><svg viewBox="0 0 10 10"><circle cx="5" cy="5" r="3.6" stroke="#fff" fill="none" stroke-width="1.3"/><circle cx="5" cy="5" r="1.3" fill="#fff"/></svg></span>
      <span>Email: anika.roswell@kvt.kiwi</span>
    </div>
    <div class="contact-row">
      <span class="icon"><svg viewBox="0 0 10 10"><path d="M2 1h2l1 2.5-1.3 1a5 5 0 0 0 2.8 2.8l1-1.3L10 7v2a1 1 0 0 1-1 1A8 8 0 0 1 1 2a1 1 0 0 1 1-1z" fill="#fff"/></svg></span>
      <span>Phone: +91-9000012345</span>
    </div>
  </div>
  <p class="footer">© 2018 | KVT Services Ltd | Privacy Policy | All Rights Reserved</p>
</section>

</body>
</html>
```